'Cradle Ahead' promotional brochure

We have designed a 6 week program to educate impending first-time parents about the things they need to know to survive the first 6 months. Sessions delivered by general practitioner/family doctor, dietician, physiotherapist, speech pathologist and psychologist. Our promotional blurb is: 'A comprehensive education program for first-time parents-to-be, delivered over 6 weeks by health professionals in your community, about everything you need to know to look after your baby (and yourself!) in the first 6 months'. I now want to put together a promotional brochure to be distributed to those couples who express an interest which will provide further details of what will be delivered in the course.
Updates
In terms of layout, I envisaged a double sided A4 size, foldable into 3 sections, but very happy to be guided on this.
Target Market(s)
To appeal to a young, well educated demographic. First time parents couples.
Industry/Entity Type
Medical
Font styles to use
Other font styles liked:
- Playfair Display
Requirements
Must have
- Playfair display font to be consistent with our logo (attached). Logo also included please. Some consistency with colours of logo please.
Nice to have
- I am a doctor, and have no creative genes! But prefer a clean and professional appearance overall. Not too cluttered in overall appearance.
Should not have
- No cheesy pictures of babies.

```html
<!DOCTYPE html>
<html lang="en">
<head>
<meta charset="utf-8">
<title>Cradle Ahead – Brochure</title>
<link rel="stylesheet" href="https://fonts.googleapis.com/css2?family=Arimo:wght@400;700&family=Playfair+Display:wght@400&display=swap">
<style>
  :root {
    --green: #7dc142;
    --green-dark: #4a8a1c;
    --green-pale: #e2f0d4;
    --grey-light: #e4e4e4;
    --grey-mid: #c9c9c9;
    --grey-bar: #7a7a7a;
    --heading-grey: #8a8a8a;
    --text: #3a3a3a;
    --white: #ffffff;
    --photo-warm: #d8c9b0;
    --photo-cool: #e6e6e3;
  }
  * { box-sizing: border-box; margin: 0; padding: 0; }
  html, body { width: 1200px; height: 848px; overflow: hidden; background: var(--white); }
  body { font-family: "Arimo", Arial, sans-serif; color: var(--text); }
  .brochure { position: relative; width: 1200px; height: 848px; overflow: hidden; }
  .panel { position: absolute; top: 0; height: 848px; }
  .panel--program { left: 0; width: 400px; }
  .panel--team { left: 400px; width: 400px; }
  .panel--cover { left: 800px; width: 400px; }

  .week-title { position: absolute; left: 24px; font-size: 24px; font-weight: 700; color: var(--heading-grey); }
  .session-block { position: absolute; left: 0; width: 400px; padding: 16px 24px; font-size: 15.5px; line-height: 1.3; }
  .session-block p + p { margin-top: 16px; }
  .session-label { font-weight: 700; font-size: 17px; }
  .session-block--pale { top: 98px; height: 146px; background: var(--green-pale); padding-top: 16px; }
  .session-block--grey { top: 342px; height: 220px; background: var(--grey-mid); padding-top: 16px; }
  .accent-block { position: absolute; left: 0; top: 566px; width: 114px; height: 282px; background: var(--green); }
  .photo { position: absolute; }
  .photo--father { left: 116px; top: 566px; width: 284px; height: 282px; background: linear-gradient(135deg, var(--photo-cool), #d4d4d2); }

  .team-title { position: absolute; left: 10px; top: 42px; font-size: 24px; font-weight: 700; color: var(--heading-grey); }
  .team-board { position: absolute; left: 0; top: 98px; width: 400px; height: 750px; background: var(--grey-light); }
  .member { position: absolute; }
  .avatar { position: absolute; width: 54px; height: 58px; background: linear-gradient(160deg, #d9c1a8, #b99a7c); border: 3px solid var(--white); }
  .name-bar { position: absolute; left: 98px; width: 198px; height: 36px; background: var(--grey-bar); color: var(--white); padding: 4px 6px; }
  .name-card { position: absolute; left: 98px; width: 198px; height: 36px; background: var(--white); color: var(--grey-bar); padding: 4px 6px; text-align: right; }
  .member-name { font-size: 15px; font-weight: 700; line-height: 1.1; }
  .member-cred { font-size: 8.5px; text-transform: uppercase; line-height: 1.3; white-space: nowrap; }

  .info { position: absolute; left: 26px; width: 360px; font-size: 14px; line-height: 1.35; color: #222; }
  .info-title { font-size: 16px; font-weight: 700; color: var(--green-dark); }
  .info--hours { top: 654px; }
  .info--contact { top: 734px; }
  .info p.gap { margin-top: 6px; }

  .brand { position: absolute; left: 26px; top: 46px; display: flex; align-items: center; gap: 14px; }
  .brand-mark { width: 52px; height: 52px; background: var(--green); }
  .brand-name { font-family: "Playfair Display", Georgia, serif; font-size: 20px; line-height: 1.05; color: #555; text-transform: uppercase; }
  .corner-block { position: absolute; left: 248px; top: 38px; width: 152px; height: 92px; background: var(--green); }
  .photo--family { left: 0; top: 136px; width: 400px; height: 316px; background: linear-gradient(120deg, #c9d6b8, var(--photo-warm) 60%, #e9dcc6); }
  .cover-band { position: absolute; left: 0; top: 456px; width: 400px; height: 392px; background: var(--green); }
  .cover-title { position: absolute; left: 0; top: 640px; width: 400px; text-align: center; font-size: 40px; font-weight: 700; color: var(--white); letter-spacing: 0.5px; text-transform: uppercase; }
</style>
</head>
<body>
<main class="brochure">

  <section class="panel panel--program">
    <h2 class="week-title" style="top:42px">Week 5</h2>
    <div class="session-block session-block--pale">
      <p><span class="session-label">Session 1</span> – Clinical Psychologist<br>
      Dr Maren Coutts will share information about bonding &amp; attachment with your baby, how to promote their social &amp; emotional development and how to manage separation anxiety. She will also discuss positive parenting approaches.</p>
    </div>
    <h2 class="week-title" style="top:280px">Week 6</h2>
    <div class="session-block session-block--grey">
      <p><span class="session-label">Session 1 –</span> Secret Men’s Business – a men-only session (including beer!) with a new father for frank discussion about the road ahead. Mums will do a shopping excursion with the GP &amp; Dietician to Greengate Market to look at baby products and food – the good and the bad!</p>
      <p><span class="session-label">Session 2 -</span> Program review, reflection and evaluation and future session planning when baby is 6 months of age.</p>
    </div>
    <div class="accent-block"></div>
    <div class="photo photo--father" role="img" aria-label="Photo of a young father cradling his newborn baby"></div>
  </section>

  <section class="panel panel--team">
    <h2 class="team-title">The Team</h2>
    <div class="team-board"></div>

    <div class="member" style="left:0;top:136px">
      <div class="avatar" style="left:40px;top:0" role="img" aria-label="Portrait of Dr Helena Marsh"></div>
      <div class="name-bar" style="top:0"><div class="member-name">Dr Helena Marsh</div><div class="member-cred">MBBS FRACGP B Sc Grad Dip Ed</div></div>
      <div class="name-card" style="top:38px"><div class="member-name">Dr Tobias Reid</div><div class="member-cred">MBBS, FRACGP, B Int Bus, GDip Econ</div></div>
      <div class="avatar" style="left:302px;top:20px" role="img" aria-label="Portrait of Dr Tobias Reid"></div>
    </div>

    <div class="member" style="left:0;top:220px">
      <div class="avatar" style="left:40px;top:0" role="img" aria-label="Portrait of Dr Orla Brennan"></div>
      <div class="name-bar" style="top:0"><div class="member-name">Dr Orla Brennan</div><div class="member-cred">MB BCh BAO NUI, FRACGP, MICGP, DRCOG</div></div>
      <div class="name-card" style="top:38px"><div class="member-name">Dr Sienna Ward</div><div class="member-cred">MBBS</div></div>
      <div class="avatar" style="left:302px;top:20px" role="img" aria-label="Portrait of Dr Sienna Ward"></div>
    </div>

    <div class="member" style="left:0;top:304px">
      <div class="avatar" style="left:40px;top:0" role="img" aria-label="Portrait of Lorraine Pike"></div>
      <div class="name-bar" style="top:0"><div class="member-name">Lorraine Pike</div><div class="member-cred">Bachelor of Podiatry and Nursing</div></div>
      <div class="name-card" style="top:38px"><div class="member-name">Dr Petra Lindqvist</div><div class="member-cred">MBBS</div></div>
      <div class="avatar" style="left:302px;top:20px" role="img" aria-label="Portrait of Dr Petra Lindqvist"></div>
    </div>

    <div class="member" style="left:0;top:388px">
      <div class="avatar" style="left:40px;top:0" role="img" aria-label="Portrait of Callum Fraser"></div>
      <div class="name-bar" style="top:0"><div class="member-name">Callum Fraser</div><div class="member-cred">B. Physiotherapy, B. Exercise Science</div></div>
      <div class="name-card" style="top:38px"><div class="member-name">Tessa Morrow</div><div class="member-cred">BA of ExSci, Doctorate of Physiotherapy</div></div>
      <div class="avatar" style="left:302px;top:20px" role="img" aria-label="Portrait of Tessa Morrow"></div>
    </div>

    <div class="member" style="left:0;top:472px">
      <div class="avatar" style="left:40px;top:0" role="img" aria-label="Portrait of Gemma Hollis"></div>
      <div class="name-bar" style="top:0"><div class="member-name">Gemma Hollis</div><div class="member-cred">Nutritionist</div></div>
      <div class="name-card" style="top:38px"><div class="member-name">Ruth Ellery</div><div class="member-cred">Paediatric Speech Pathologist</div></div>
      <div class="avatar" style="left:302px;top:20px" role="img" aria-label="Portrait of Ruth Ellery"></div>
    </div>

    <div class="member" style="left:0;top:556px">
      <div class="avatar" style="left:40px;top:0" role="img" aria-label="Portrait of Nadia Trent"></div>
      <div class="name-bar" style="top:0"><div class="member-name">Nadia Trent</div><div class="member-cred">B. Hm &amp; ExSci / Grad Dip. Clinical Ex Phys</div></div>
    </div>

    <div class="info info--hours">
      <h3 class="info-title">OPENING HOURS</h3>
      <p>Monday to Friday: 8:30am – 5:00pm</p>
      <p>Saturday: 8:00am – 12:00pm</p>
      <p>Sunday &amp; Public Holidays:&nbsp; Closed</p>
    </div>
    <div class="info info--contact">
      <h3 class="info-title">CONTACT INFORMATION</h3>
      <p>Wattlebrook Village Centre, Shop 7</p>
      <p>215 Banksia Parade, Wattlebrook NSW 2999</p>
      <p class="gap">Phone: 02 5550 1234 &nbsp;• Fax: 02 5550 1235</p>
      <p>Email: hello@wattlebrookhealth.example</p>
    </div>
  </section>

  <section class="panel panel--cover">
    <div class="brand">
      <span class="brand-mark"></span>
      <span class="brand-name">Wattlebrook<br>Health &amp;<br>Medical</span>
    </div>
    <div class="corner-block"></div>
    <div class="photo photo--family" role="img" aria-label="Photo of smiling parents holding their baby outdoors"></div>
    <div class="cover-band"></div>
    <h1 class="cover-title">Cradle Ahead</h1>
  </section>

</main>
</body>
</html>
```